Magazine Ad for the Waste Industry

We need a full page ad design that will help us introduce our new engine cooling system into the Waste market. This system helps regulate engine temperatures for large trash trucks with its advanced technology and durable. We would like this ad to make an impact and stand out from the more cluttered looking ads that are seen in trade magazines.
The project must be submitted in either InDesign or Photoshop files.

Target Market(s)

Waste Industry, Trash truck manufacturers

Industry/Entity Type

Waste Management

Font styles to use
Sans Serif

Colors
0255a3

Requirements
Must have
• The text and images attached with a more modern industrial/masculine feel.
• Our Company colors are...
• Blue (RGB 25, 76, 159)
• Gray (RGB 129, 130, 133)
• White and black as accents as needed
• SIZING
• Spread Bleed: 9.5" x 11.375"
Nice to have
• I attached two files for a font that we have used in the past. Another font we use commonly is Ariel.

```html
<!DOCTYPE html>
<html lang="en">
<head>
<meta charset="utf-8">
<title>Advanced Electric Engine Cooling – Trade Ad</title>
<link rel="stylesheet" href="https://fonts.googleapis.com/css2?family=Krona+One&family=Oswald:wght@500&display=swap">
<style>
  :root {
    --brand-blue: #1a4ba3;
    --deep-blue: #1a449f;
    --mid-blue: #4a74c6;
    --sky: #f1f3f9;
    --white: #ffffff;
    --canvas: #dcdcdc;
  }
  * { box-sizing: border-box; margin: 0; padding: 0; }
  html, body { width: 1200px; height: 1200px; overflow: hidden; background: var(--canvas); }
  .ad-page {
    position: absolute; left: 99px; top: 0;
    width: 1182px; height: 1415px;
    transform: scale(0.84806); transform-origin: top left;
    background: linear-gradient(180deg, var(--sky) 0%, #c9d4ee 14%, #6f90d6 27%, var(--mid-blue) 45%, #3a62b8 70%, var(--deep-blue) 100%);
    overflow: hidden;
  }
  .headline {
    position: absolute; left: 91px; top: 70px;
    font-family: "Krona One", sans-serif; color: var(--brand-blue);
    font-size: 60px; line-height: 62px; text-transform: uppercase; white-space: nowrap;
  }
  .web-address {
    position: absolute; left: 91px; top: 272px;
    font-family: "Krona One", sans-serif; color: var(--brand-blue);
    font-size: 33px; white-space: nowrap;
  }
  .company-name {
    position: absolute; left: 880px; top: 78px; width: 250px; text-align: center;
    font-family: "Krona One", sans-serif; color: var(--brand-blue); font-size: 34px;
  }
  .sub-brand-name {
    position: absolute; left: 880px; top: 250px; width: 250px; text-align: center;
    font-family: "Krona One", sans-serif; color: var(--brand-blue); font-size: 26px;
  }
  .frame { position: absolute; left: 0; top: 0; }
  .benefits { position: absolute; left: 71px; top: 455px; width: 500px; list-style: none; }
  .benefit { height: 155.5px; display: flex; flex-direction: column; align-items: center; }
  .benefit-icon { width: 94px; height: 94px; }
  .benefit-label {
    margin-top: 6px;
    font-family: "Oswald", sans-serif; font-weight: 500; color: var(--white);
    font-size: 29px; line-height: 36px; text-transform: uppercase; letter-spacing: 0.2px; white-space: nowrap;
  }
  .product-visual {
    position: absolute; left: 561px; top: 612px; width: 520px; height: 573px;
    background: linear-gradient(135deg, #3a3c40 0%, #1d1e21 60%, #2c2e32 100%);
    border-radius: 4px;
  }
</style>
</head>
<body>
<main class="ad-page">
  <h1 class="headline">Advanced<br>Electric Engine<br>Cooling</h1>
  <p class="web-address">www.norvane-corp.com/refuse</p>

  <p class="company-name">NORVANE</p>
  <p class="sub-brand-name">ECO-LITE</p>

  <svg class="frame" width="1182" height="1415" viewBox="0 0 1182 1415" aria-hidden="true">
    <g fill="none" stroke="#ffffff" stroke-width="3">
      <polyline points="95,435 547,435"/>
      <polyline points="321,435 321,342 1088,342 1088,1333 321,1333 321,1241"/>
      <polyline points="95,1241 547,1241"/>
    </g>
  </svg>

  <ul class="benefits">
    <li class="benefit">
      <svg class="benefit-icon" viewBox="0 0 94 94" aria-hidden="true">
        <circle cx="47" cy="47" r="46" fill="#fff"/>
        <circle cx="47" cy="47" r="40" fill="none" stroke="#1a4ba3" stroke-width="2" stroke-dasharray="2 3"/>
        <path d="M28 44a19 19 0 0 1 33-10" fill="none" stroke="#1a4ba3" stroke-width="7"/>
        <path d="M56 26l12 4-6 11z" fill="#1a4ba3"/>
        <path d="M66 50a19 19 0 0 1-33 10" fill="none" stroke="#1a4ba3" stroke-width="7"/>
        <path d="M38 68l-12-4 6-11z" fill="#1a4ba3"/>
      </svg>
      <span class="benefit-label">Fully Reversible Fans</span>
    </li>
    <li class="benefit">
      <svg class="benefit-icon" viewBox="0 0 94 94" aria-hidden="true">
        <circle cx="47" cy="47" r="46" fill="#fff"/>
        <circle cx="47" cy="47" r="40" fill="none" stroke="#1a4ba3" stroke-width="2" stroke-dasharray="2 3"/>
        <circle cx="47" cy="47" r="24" fill="none" stroke="#1a4ba3" stroke-width="5"/>
        <rect x="26" y="43" width="42" height="8" rx="4" fill="#1a4ba3"/>
        <line x1="30" y1="64" x2="64" y2="30" stroke="#1a4ba3" stroke-width="5"/>
      </svg>
      <span class="benefit-label">Eliminate Preventative Maintenance</span>
    </li>
    <li class="benefit">
      <svg class="benefit-icon" viewBox="0 0 94 94" aria-hidden="true">
        <circle cx="47" cy="47" r="46" fill="#fff"/>
        <circle cx="47" cy="47" r="40" fill="none" stroke="#1a4ba3" stroke-width="2" stroke-dasharray="2 3"/>
        <path d="M26 60l8-18 22-6 8 8-20 6-6 12z" fill="#1a4ba3"/>
        <path d="M62 42l6 6" stroke="#1a4ba3" stroke-width="5"/>
        <circle cx="70" cy="55" r="3" fill="#1a4ba3"/>
      </svg>
      <span class="benefit-label">Average 8% Fuel Economy</span>
    </li>
    <li class="benefit">
      <svg class="benefit-icon" viewBox="0 0 94 94" aria-hidden="true">
        <circle cx="47" cy="47" r="46" fill="#fff"/>
        <circle cx="47" cy="47" r="40" fill="none" stroke="#1a4ba3" stroke-width="2" stroke-dasharray="2 3"/>
        <polyline points="26,56 40,40 46,56 62,36" fill="none" stroke="#1a4ba3" stroke-width="7" stroke-linejoin="round"/>
        <path d="M56 30l12-2-2 12z" fill="#1a4ba3"/>
      </svg>
      <span class="benefit-label">Increase Horsepower</span>
    </li>
    <li class="benefit">
      <svg class="benefit-icon" viewBox="0 0 94 94" aria-hidden="true">
        <circle cx="47" cy="47" r="46" fill="#fff"/>
        <circle cx="47" cy="47" r="40" fill="none" stroke="#1a4ba3" stroke-width="2" stroke-dasharray="2 3"/>
        <path d="M26 40h8l12-10v34l-12-10h-8z" fill="#1a4ba3"/>
        <path d="M54 39a10 10 0 0 1 0 16M59 33a18 18 0 0 1 0 28" fill="none" stroke="#1a4ba3" stroke-width="4" stroke-linecap="round"/>
      </svg>
      <span class="benefit-label">Quieter Residential Operation</span>
    </li>
  </ul>

  <div class="product-visual" role="img" aria-label="Electric engine cooling module: black radiator frame with four caged electric fans"></div>
</main>
</body>
</html>
```